Company or website name
- Harwood & Beale LLP
- Links to the website
- harwoodbeale-example.com
- Describe your company and organization and target audience
- lawyers and clients in the need of lawyer for defective products etc
- The design should have the following
- yes
- Other Facts

```html
<!DOCTYPE html>
<html lang="en">
<head>
<meta charset="utf-8">
<title>Harwood &amp; Beale LLP</title>
<link href="https://fonts.googleapis.com/css2?family=Source+Sans+3:wght@400;600;700&family=Copse&family=Itim&display=swap" rel="stylesheet">
<style>
:root{
  --navy:#0d236b;
  --navy-deep:#0a1a52;
  --blue:#123e8c;
  --sky:#0ea2ee;
  --sky-light:#29b7f7;
  --orange:#f07c1a;
  --text:#3a3a3a;
  --panel:#f7f7f7;
  --white:#ffffff;
}
*{margin:0;padding:0;box-sizing:border-box}
html,body{width:818px;height:1200px;overflow:hidden;background:var(--white)}
body{position:relative;font-family:"Source Sans 3",Arial,sans-serif;color:var(--text)}
.abs{position:absolute}
.topnav{left:0;top:0;width:818px;height:32px;background:var(--navy);border-bottom:2px solid #3d5aa8}
.topnav a{position:absolute;top:8px;color:var(--white);font-weight:700;font-size:11.5px;text-decoration:none;letter-spacing:.2px}
.hero{left:0;top:32px;width:818px;height:546px;background:linear-gradient(90deg,#5d7186 0%,#a9b6c2 30%,#c9d0d6 50%,#3d3f45 75%,#546170 100%)}
.header-card{left:68px;top:34px;width:682px;height:65px;background:var(--white);border-radius:0 0 8px 8px;box-shadow:0 4px 8px rgba(0,0,0,.35)}
.brand-dot{left:12px;top:14px;width:38px;height:38px;border-radius:50%;background:var(--blue)}
.brand-name{left:75px;top:16px;font-size:23px;font-weight:700;color:var(--orange);white-space:nowrap}
.search{left:548px;top:11px;width:120px;height:18px;border:1px solid #ccc;border-radius:2px;font-size:8px;color:#888;padding:3px 4px}
.search svg{position:absolute;right:3px;top:3px}
.phone{left:585px;top:43px;font-size:11.5px;color:#555;display:flex;align-items:center;gap:3px}
.tagline{left:84px;top:194px;width:324px;height:150px;background:var(--navy);padding:20px 17px 0 19px;color:var(--white)}
.tagline h1{font-family:"Itim",cursive;font-weight:400;font-size:21px;color:#cfe0ff;margin-bottom:12px;white-space:nowrap}
.tagline p{font-size:10.4px;line-height:13.6px;text-align:justify}
.arrow{top:240px}
.features{left:68px;top:462px;width:682px;height:116px;background:linear-gradient(#0ca0ef,#2ab9f6);border-top:7px solid var(--navy)}
.feature{position:absolute;top:14px;width:150px;color:var(--white)}
.feature h2{display:flex;align-items:center;gap:5px;font-family:"Copse",serif;font-weight:400;font-size:14.5px;margin-bottom:7px;white-space:nowrap}
.feature p{font-family:"Copse",serif;font-size:9.5px;line-height:12.3px;text-align:justify}
.feature-sep{position:absolute;top:20px;width:1px;height:88px;background:rgba(255,255,255,.3)}
.about{left:68px;top:578px;width:682px;height:246px;background:var(--panel);box-shadow:0 2px 3px rgba(0,0,0,.08)}
.about h2{position:absolute;left:11px;top:22px;font-size:22px;font-weight:400;color:var(--blue)}
.about p{position:absolute;left:11px;width:430px;font-family:Arial,sans-serif;font-size:9.8px;line-height:15px;color:#444}
.divider{left:530px;top:578px;width:1px;height:256px;background:#ddd;box-shadow:1px 0 0 #fff}
.news h3{position:absolute;left:546px;top:588px;font-size:13px;font-weight:400;color:var(--blue)}
.news-rule{left:543px;top:616px;width:185px;height:1px;background:#bbb}
.news-item .thumb{position:absolute;width:49px;height:37px;background:linear-gradient(135deg,#dfe6ee,#5a8fc6 55%,#263a55)}
.news-item h4{position:absolute;left:595px;font-size:11.5px;font-weight:400;color:var(--blue)}
.news-item p{position:absolute;left:595px;width:140px;font-size:9.8px;line-height:13.8px;color:#444}
.more-line{left:578px;top:793px;width:125px;height:1px;background:linear-gradient(90deg,transparent,#999,transparent)}
.more{left:614px;top:785px;width:45px;height:16px;background:#444;border-radius:2px;color:#fff;font-size:9.5px;line-height:16px;padding-left:13px}
.more::before{content:"›";position:absolute;left:4px;top:-1px;color:#aaa}
.quote{font-family:Georgia,serif;font-size:38px;font-weight:700;color:var(--blue);line-height:1}
.avatar{left:130px;top:873px;width:92px;height:92px;border-radius:50%;background:radial-gradient(circle at 50% 40%,#c9b3a2,#6d625c 60%,#e6e6e6 62%);border:2px solid #e8e8e8;box-shadow:0 1px 3px rgba(0,0,0,.3)}
.testimonial h3{position:absolute;left:244px;top:866px;font-size:13px;font-weight:400;color:var(--blue)}
.testimonial p{position:absolute;left:244px;width:487px;font-size:9.9px;line-height:13px;text-align:justify;color:#222}
.footer{left:0;top:1046px;width:818px;height:154px;background:radial-gradient(ellipse at 50% 120%,#1d3f9a,var(--navy-deep) 70%);border-top:2px solid #d9d9d9;color:var(--white)}
.footer h4{position:absolute;font-size:10.5px;font-weight:400;letter-spacing:.3px}
.footer .lines{position:absolute;left:80px;top:44px;font-size:10px;line-height:13px;letter-spacing:.3px}
.footer .call{position:absolute;left:80px;top:104px;font-size:10.5px}
.footer ul{position:absolute;left:419px;top:49px;list-style:none;font-size:8.6px;line-height:12.3px}
.social{position:absolute;left:624px;display:flex;align-items:center;gap:6px;font-size:10px}
.social span.ring{width:18px;height:18px;border:2px solid #fff;border-radius:50%}
</style>
</head>
<body>

<nav class="abs topnav">
  <a style="left:78px">HOME</a><a style="left:164px">ABOUT US</a><a style="left:277px">SOLUTIONS</a><a style="left:394px">NEWS</a><a style="left:481px">CLIENTS</a><a style="left:578px">CAREERS</a><a style="left:677px">CONTACT US</a>
</nav>

<div class="abs hero" role="img" aria-label="Photo of a businesswoman in an office with colleagues in the background"></div>

<header class="abs header-card">
  <div class="abs brand-dot"></div>
  <div class="abs brand-name">Harwood &amp; Beale LLP</div>
  <div class="abs search">Search
    <svg width="10" height="10" viewBox="0 0 10 10"><circle cx="4" cy="4" r="3" fill="none" stroke="#555" stroke-width="1.4"/><line x1="6.2" y1="6.2" x2="9" y2="9" stroke="#555" stroke-width="1.6"/></svg>
  </div>
  <div class="abs phone">
    <svg width="8" height="11" viewBox="0 0 8 11"><path d="M2 0 L4 2.5 L3 4 Q3.5 6 5 7.5 L6.5 6.8 L8 9 L6 11 Q1 9 0 2 Z" fill="#1c4a96"/></svg>555-010-2040
  </div>
</header>

<section class="abs tagline">
  <h1>A beautiful tag line goes here</h1>
  <p>Lorem ipsum dolor sit amet, consectetuer adipiscing elit, sed diam nonummy nibh euismod tincidunt ut laoreet dolore magna aliquam erat volutpat. Ut wisi enim ad minim veniam, quis nostrud exerci tation ullamcorper suscipit lobortis.</p>
</section>

<svg class="abs arrow" style="left:42px" width="27" height="36" viewBox="0 0 27 36"><path d="M12 2 L2 18 L12 34 M25 2 L15 18 L25 34" fill="none" stroke="#0d3f94" stroke-width="5"/></svg>
<svg class="abs arrow" style="left:750px" width="27" height="36" viewBox="0 0 27 36"><path d="M2 2 L12 18 L2 34 M15 2 L25 18 L15 34" fill="none" stroke="#0d3f94" stroke-width="5"/></svg>

<section class="abs features">
  <div class="feature" style="left:10px"><h2><svg width="26" height="22" viewBox="0 0 26 22"><path d="M3 14 V10 a10 9 0 0 1 20 0 V14" fill="none" stroke="#fff" stroke-width="2"/><rect x="2" y="12" width="6" height="9" rx="2" fill="none" stroke="#fff" stroke-width="2"/><rect x="18" y="12" width="6" height="9" rx="2" fill="none" stroke="#fff" stroke-width="2"/></svg>HEADING HERE</h2>
    <p>Lorem ipsum dolor sit amet, consectetuer adipiscing elit, sed diam nonummy nibh euismod tincidunt.</p></div>
  <div class="feature-sep" style="left:164px"></div>
  <div class="feature" style="left:180px"><h2><svg width="18" height="22" viewBox="0 0 18 22"><path d="M3 2 Q2 12 12 13 Z" fill="none" stroke="#fff" stroke-width="1.8"/><path d="M8 13 L4 20 H16" fill="none" stroke="#fff" stroke-width="1.8"/><line x1="9" y1="7" x2="15" y2="2" stroke="#fff" stroke-width="1.8"/></svg>HEADING HERE</h2>
    <p>Lorem ipsum dolor sit amet, consectetuer adipiscing elit, sed diam nonummy nibh euismod tincidunt.</p></div>
  <div class="feature-sep" style="left:334px"></div>
  <div class="feature" style="left:351px"><h2><svg width="22" height="22" viewBox="0 0 22 22"><rect x="1" y="2" width="20" height="15" fill="none" stroke="#fff" stroke-width="1.8"/><line x1="4" y1="20" x2="18" y2="20" stroke="#fff" stroke-width="1.8"/><path d="M8 6 L13 10 L10 10 L12 13" fill="none" stroke="#fff" stroke-width="1.4"/></svg>HEADING HERE</h2>
    <p>Lorem ipsum dolor sit amet, consectetuer adipiscing elit, sed diam nonummy nibh euismod tincidunt.</p></div>
  <div class="feature-sep" style="left:505px"></div>
  <div class="feature" style="left:521px"><h2><svg width="22" height="22" viewBox="0 0 22 22"><rect x="2" y="7" width="18" height="13" rx="2" fill="none" stroke="#fff" stroke-width="1.8"/><rect x="5" y="10" width="12" height="7" fill="none" stroke="#fff" stroke-width="1.4"/><path d="M7 1 L11 6 L15 1" fill="none" stroke="#fff" stroke-width="1.6"/></svg>HEADING HERE</h2>
    <p>Lorem ipsum dolor sit amet, consectetuer adipiscing elit, sed diam nonummy nibh euismod tincidunt.</p></div>
</section>

<section class="abs about">
  <h2>Harwood &amp; Beale LLP</h2>
  <p style="top:56px">Lorem ipsum dolor sit amet, consectetuer adipiscing elit, sed diam nonummy nibh euismod tincidunt ut laoreet dolore magna aliquam erat volutpat. Ut wisi enim ad minim veniam, quis nostrud exerci tation ullamcorper suscipit lobortis nisl ut aliquip ex ea commodo consequat. Duis autem vel eum iriure dolor in hendrerit in vulputate velit esse molestie consequat, vel illum dolore eu feugiat nulla facilisis at vero eros et accumsan et iusto odio dignissim qui blandit praesent luptatum zzril delenit augue duis dolore te feugait nulla facilisi.</p>
  <p style="top:148px">Nam liber tempor cum soluta nobis eleifend option congue nihil imperdiet doming id quod mazim placerat facer possim assum.Nam liber tempor cum soluta nobis eleifend option congue nihil imperdiet doming id quod mazim placerat facer possim assum.</p>
</section>
<div class="abs divider"></div>

<aside class="news">
  <h3>Latest News</h3>
  <div class="abs news-rule"></div>
  <div class="news-item">
    <div class="thumb" style="left:541px;top:638px" role="img" aria-label="Photo of hands holding a globe"></div>
    <h4 style="top:627px">Heading goes here</h4>
    <p style="top:643px">Lorem ipsum dolor sit amet, consectetuer adipiscing elit, sed diam nonummy.</p>
  </div>
  <div class="news-item">
    <div class="thumb" style="left:541px;top:703px" role="img" aria-label="Photo of hands holding a globe"></div>
    <h4 style="top:697px">Heading goes here</h4>
    <p style="top:713px">Lorem ipsum dolor sit amet, consectetuer adipiscing elit, sed diam nonummy.</p>
  </div>
  <div class="abs more-line"></div>
  <div class="abs more">More</div>
</aside>

<section class="testimonial">
  <div class="abs quote" style="left:76px;top:852px">“</div>
  <div class="abs avatar" role="img" aria-label="Portrait photo of the client"></div>
  <h3>Martin Cole</h3>
  <p style="top:890px">Lorem ipsum dolor sit amet, consectetuer adipiscing elit, sed diam nonummy nibh euismod tincidunt ut laoreet dolore magna aliquam erat volutpat. Ut wisi enim ad minim veniam, quis nostrud exerci tation ullamcorper suscipit lobortis nisl ut aliquip ex ea commodo consequat. Lorem ipsum dolor sit amet, consectetuer adipiscing elit, sed diam nonummy nibh euismod tincidunt ut laoreet dolore magna aliquam erat volutpat.</p>
  <p style="top:956px">Nora Lind, Brightwell Supply</p>
  <div class="abs quote" style="left:719px;top:974px">”</div>
</section>

<footer class="abs footer">
  <h4 style="left:80px;top:13px">CONTACT US</h4>
  <div class="lines">XXXXXXXXXXXXXXXXXXX<br>XXXXXXXXXXXXXXXXX<br>XXXXXXXXXXXXXXXXXX<br>XXXXXXXXXXXXXXX</div>
  <div class="call">CALL US NOW : 0555-010-204</div>
  <h4 style="left:419px;top:21px">BROWSE SITE</h4>
  <ul><li>Home</li><li>About us</li><li>Solutions</li><li>News</li><li>Careers</li><li>Contact us</li></ul>
  <h4 style="left:623px;top:21px">FOLLOW US</h4>
  <div class="social" style="top:47px"><span class="ring"></span>Chirp</div>
  <div class="social" style="top:78px"><span class="ring"></span>Friendbook</div>
</footer>

</body>
</html>
```